Akademie für Lichtwegkunde
Zielgruppe
Ich biete die beiden Seminare 'Kraftquell am Werktag' und 'Feinsinn am Werktag' an. Die Zielgruppe sind spirituell interessierte Leute.
Aufgabenstellung
Die Anzeige sollte mehr oder weniger mit den Farben meiner Webseite übereinstimmen (www.sonnenpfad-raum.ch).
Grösse der Anzeige:
breit: 121mm
hoch: 124mm
Die Anzeige sollte mein persönliches Bild und das Logo enthalten.
Text:
Feinsinn am Werktag:
Seminare zur Förderung Ihrer Intuition. Entdecken Sie Ihre eigene Medialität und lernen Sie diese gezielt im Alltag einzusetzen.
26./27. August 2017
11./12. November 2017
Kraftquell am Werktag:
Seminare für energetisches Heilen. Lernen Sie sich und andere Menschen energetisch zu begleiten.
16./17. September 2017
9./10. Dezember 2017
2 für 1 - Aktion:
Kommen Sie zu zweit und bezahlen Sie nur für eine Person
(gültig bis Ende 2017)
Webseite:
www.sonnenpfad-raum.ch
Seminarort: Grünholdau, 3286 Lorbachtal, Schweiz

```html
<!DOCTYPE html>
<html lang="de">
<head>
<meta charset="utf-8">
<title>Akademie für Lichtwegkunde – Anzeige 2 für 1</title>
<link rel="stylesheet" href="https://fonts.googleapis.com/css2?family=Nunito+Sans:wght@400;600;700;800&display=swap">
<style>
  :root {
    --stage: #d6d6d6;
    --header-blue: #4f86c6;
    --band-blue: #4a82c4;
    --body-blue: #cbdaf0;
    --label-blue: #5a8fcd;
    --accent-orange: #e06d1a;
    --text-dark: #2e2e2e;
    --white: #ffffff;
    --photo-light: #c9c9c9;
    --photo-dark: #3c3c3c;
  }
  * { margin: 0; padding: 0; box-sizing: border-box; }
  html, body { width: 1200px; height: 801px; overflow: hidden; }
  body {
    background: var(--stage);
    font-family: "Nunito Sans", Arial, sans-serif;
    position: relative;
  }
  .ad {
    position: absolute;
    left: 220px;
    top: 11px;
    width: 761px;
    height: 780px;
    background: var(--white);
    overflow: hidden;
  }
  .ad-header {
    position: absolute; left: 0; top: 0; width: 100%; height: 177px;
    background: var(--header-blue);
    color: var(--white);
  }
  .offer-kicker {
    position: absolute; left: 37px; top: 33px;
    font-size: 27px; font-weight: 600; line-height: 32px; white-space: nowrap;
  }
  .offer-headline {
    position: absolute; left: 37px; top: 67px;
    font-size: 36px; font-weight: 800; line-height: 39px; white-space: nowrap;
  }
  .promo-ribbon { position: absolute; right: 0; top: 0; }
  .ad-body {
    position: absolute; left: 0; top: 177px; width: 100%; height: 399px;
    background: var(--body-blue);
  }
  .seminar { position: absolute; top: 34px; color: var(--text-dark); }
  .seminar--intuition { left: 37px; }
  .seminar--healing { left: 400px; }
  .seminar-label {
    color: var(--label-blue); font-size: 20.5px; line-height: 27px; font-weight: 400; white-space: nowrap;
  }
  .seminar-title {
    color: var(--accent-orange); font-size: 29.5px; font-weight: 700;
    line-height: 33px; margin-top: 2px; white-space: nowrap;
  }
  .seminar-text {
    font-size: 20.5px; line-height: 27px; margin-top: 27px; white-space: nowrap;
  }
  .seminar-dates {
    position: absolute; top: 230px; left: 0;
    font-size: 20.5px; line-height: 26px; white-space: nowrap;
  }
  .venue {
    position: absolute; left: 37px; top: 339px;
    font-size: 20.5px; line-height: 26px; color: var(--text-dark); white-space: nowrap;
  }
  .website {
    position: absolute; right: 38px; top: 340px;
    font-size: 17px; line-height: 26px; font-weight: 700; color: var(--accent-orange); white-space: nowrap;
  }
  .ad-band {
    position: absolute; left: 0; top: 576px; width: 100%; height: 27px;
    background: var(--band-blue);
  }
  .portrait {
    position: absolute; left: 0; top: 603px; width: 200px; height: 177px;
    background: radial-gradient(ellipse at 55% 45%, var(--photo-light) 0%, #8d8d8d 55%, var(--photo-dark) 100%);
  }
  .brand {
    position: absolute; right: 40px; top: 665px;
    display: flex; align-items: center; gap: 14px;
  }
  .brand-dot {
    width: 44px; height: 44px; border-radius: 50%; background: var(--header-blue);
  }
  .brand-name {
    font-size: 27px; font-weight: 700; color: var(--header-blue); white-space: nowrap;
  }
</style>
</head>
<body>
  <article class="ad">
    <header class="ad-header">
      <p class="offer-kicker">2 für 1</p>
      <h1 class="offer-headline">Kommen Sie zu zweit und<br>bezahlen Sie nur für eine Person</h1>
    </header>

    <svg class="promo-ribbon" width="200" height="200" viewBox="0 0 200 200" aria-label="Aktion, gültig bis 31.12.2017">
      <polygon points="37,0 89,0 200,111 200,163" fill="#ffffff"/>
      <text x="141" y="72" transform="rotate(45 141 72)" text-anchor="middle" dominant-baseline="middle"
            font-family="Nunito Sans, Arial, sans-serif" font-size="26" font-weight="800" fill="#4f86c6">Aktion</text>
      <text x="99" y="100" transform="rotate(45 99 100)" text-anchor="middle" dominant-baseline="middle"
            font-family="Nunito Sans, Arial, sans-serif" font-size="13" font-weight="400" fill="#ffffff">gültig bis 31.12.2017</text>
    </svg>

    <section class="ad-body">
      <div class="seminar seminar--intuition">
        <p class="seminar-label">Feinsinn am Werktag</p>
        <h2 class="seminar-title">Seminar zur Förderung<br>Ihrer Intuition</h2>
        <p class="seminar-text">Entdecken Sie Ihre eigene<br>Medialität und lernen Sie diese<br>gezielt im Alltag einzusetzen.</p>
        <p class="seminar-dates">26. bis 27. August 2017<br>11. bis 12. November 2017</p>
      </div>
      <div class="seminar seminar--healing">
        <p class="seminar-label">Kraftquell am Werktag</p>
        <h2 class="seminar-title">Seminar für<br>energetisches Heilen</h2>
        <p class="seminar-text">Lernen Sie sich und andere<br>Menschen energetisch zu<br>begleiten.</p>
        <p class="seminar-dates">16. bis 17. September 2017<br>9. bis 10. Dezember 2017</p>
      </div>
      <p class="venue">Seminarort: Grünholdau, 3286 Lorbachtal, Schweiz</p>
      <p class="website">www.sonnenpfad-raum.ch</p>
    </section>

    <div class="ad-band"></div>

    <div class="portrait" role="img" aria-label="Schwarzweiss-Porträt des Seminarleiters"></div>

    <div class="brand">
      <span class="brand-dot"></span>
      <span class="brand-name">Akademie für Lichtwegkunde</span>
    </div>
  </article>
</body>
</html>
```